KVO-Business Card Design

I need a modern, professional business card design that includes my logo as the main feature, maybe the entire background with the contact info overlaying or even contact info on the back and the logo full frontal

Neat and organized placement of contact information

Would like to see options in black and white

Target Market(s)

real estate Developers, Construction managers, business and home owners

Industry/Entity Type

Construction

Contact Information for Business Card

KVO Construction
Danny Ferrante
General Contractor

Office: 1-888-902-7315 Ext #1
Cell: 215-730-4162
Fax: 1-888-902-7315

Font styles to use
Serif

Requirements
Must have
• title
• office #
• cell #
• Email
• website
Nice to have
• fax

```html
<!DOCTYPE html>
<html lang="en">
<head>
<meta charset="utf-8">
<title>KVO Construction – Business Card</title>
<link rel="stylesheet" href="https://fonts.googleapis.com/css2?family=Roboto:wght@400;700;900&family=Roboto+Mono:wght@400;500&display=swap">
<style>
  :root {
    --backdrop: #2a5f40;
    --card: #ffffff;
    --brand-green: #1f9a46;
    --brand-deep: #17793a;
    --ink: #1d1d1d;
    --muted: #555555;
  }
  * { margin: 0; padding: 0; box-sizing: border-box; }
  html, body { width: 1200px; height: 900px; overflow: hidden; }
  body {
    background: var(--backdrop);
    font-family: "Roboto", Arial, sans-serif;
    position: relative;
  }
  .card {
    position: absolute;
    left: 290px;
    width: 620px;
    height: 354px;
    background: var(--card);
    box-shadow: 0 10px 24px rgba(0, 0, 0, 0.28);
  }
  .card--front { top: 70px; }
  .card--back  { top: 476px; }

  .brand {
    display: flex;
    align-items: center;
    gap: 14px;
    color: var(--brand-green);
    font-weight: 900;
    letter-spacing: 0.5px;
  }
  .brand__mark {
    background: var(--brand-green);
    flex: none;
  }
  .card--front .brand {
    position: absolute;
    left: 0; right: 0; top: 0; bottom: 0;
    justify-content: center;
    font-size: 40px;
  }
  .card--front .brand__mark { width: 40px; height: 40px; }

  .card--back .brand {
    position: absolute;
    right: 36px;
    top: 48px;
    font-size: 24px;
    gap: 10px;
  }
  .card--back .brand__mark { width: 24px; height: 24px; }

  .contact {
    position: absolute;
    left: 40px;
    bottom: 34px;
  }
  .contact__name {
    color: var(--brand-green);
    font-weight: 900;
    font-size: 24px;
    letter-spacing: 0.3px;
    text-transform: uppercase;
  }
  .contact__title {
    font-family: "Roboto Mono", monospace;
    font-size: 12px;
    color: var(--ink);
    margin-top: 2px;
  }
  .contact__lines {
    margin-top: 20px;
    font-family: "Roboto Mono", monospace;
    font-size: 14px;
    line-height: 1.45;
    color: var(--ink);
  }
  .contact__row { display: flex; }
  .contact__label { width: 72px; }
  .contact__web {
    margin-top: 14px;
    font-family: "Roboto Mono", monospace;
    font-weight: 500;
    font-size: 13px;
    color: var(--brand-green);
  }
</style>
</head>
<body>
  <section class="card card--front" aria-label="Business card front">
    <div class="brand">
      <span class="brand__mark"></span>
      <span class="brand__name">KVO Construction</span>
    </div>
  </section>

  <section class="card card--back" aria-label="Business card back">
    <div class="brand">
      <span class="brand__mark"></span>
      <span class="brand__name">KVO Construction</span>
    </div>

    <div class="contact">
      <p class="contact__name">Danny Ferrante</p>
      <p class="contact__title">General Contractor</p>
      <div class="contact__lines">
        <p class="contact__row"><span class="contact__label">Office</span><span>1-888-902-7315 Ext #1</span></p>
        <p class="contact__row"><span class="contact__label">Cell</span><span>215-730-4162</span></p>
        <p class="contact__row"><span class="contact__label">Fax</span><span>1-888-902-7315</span></p>
        <p class="contact__row"><span>danny@KVOConstruction.com</span></p>
      </div>
      <p class="contact__web">www.KVOConstruction.com</p>
    </div>
  </section>
</body>
</html>
```